Awesome Podcast Artwork Needed :-)

I need an AWESOME piece of podcast artwork for a new podcast called "Keys To The Porch" :-)
The Podcast teaches "new" property investors... or people just starting out... the basics of property investing (real estate) by sharing tips, tricks, strategies, interviews etc.
I have a logo that I'm kind of happy with and have attached examples of it here labelled "Examples Of Logo". It basically consists of four houses hanging on some thread and although I'm certainly not saying you must use it. If you do want to use it, I would be open to you "modernising" it a bit - if needed - or rearranging the house images in a line (horizontally or vertically) or in a square... or indeed in anyway you feel works
In terms of design, I confess I'm really not sure what I want - only I certainly do want to give a sense my Podcast is about "Property Investing".
I have included 2 examples of artwork that my competition uses labelled "Competition Artwork 1&2". I have also included "My Attempt" at doing this... which I know isn't very good - because you can't clearly see the words and to be honest - it looks weak next to other podcast artwork (for example the "Beyond Brick Ledgers" artwork that I have included here). I have attached a mock up of a "Simulated Tunewell Screen" so you can see what I mean when I say my example looks weak compared to the others.
Lastly here's my new website (it's not yet out there) but that may give you some ideas of what I like: https://keystotheporch.example/home/
I'm excited to see what you come up with :-)
PS. The artwork needs to be 3000x3000 pixels with a DPI of 72
Target Market(s)
New property investors - people who want to learn how to invest in property (real estate)
Requirements
Must have
- The name "Keys To The Porch"
Nice to have
- If my logo... or a variation on my logo can be incorporated - that would be good - but not essential. I've attached examples but will happily consider modifications.
- Please do not feel however that you must include the logo.

```html
<!DOCTYPE html>
<html lang="en">
<head>
<meta charset="utf-8">
<title>Keys To The Porch – Podcast Cover</title>
<link rel="stylesheet" href="https://fonts.googleapis.com/css2?family=Archivo+Black&family=Itim&family=Open+Sans:wght@400&family=Roboto+Condensed:wght@700&display=swap">
<style>
  :root {
    --page: #ffffff;
    --frame: #111111;
    --sky-top: #bccfdc;
    --sky-bottom: #d4e0e7;
    --building: #eef0f1;
    --house-blue: #9fb3cd;
    --roof-blue: #9cb0cb;
    --accent-orange: #da8700;
    --ink: #2b2b2b;
    --band-black: #0d0d0d;
    --cream: #e6e2dc;
    --url-yellow: #e4e02a;
    --suit-navy: #26324a;
    --denim: #4f6f9c;
  }
  html, body {
    margin: 0;
    padding: 0;
    width: 1200px;
    height: 1200px;
    overflow: hidden;
    background: var(--page);
  }
  .cover {
    position: relative;
    width: 1200px;
    height: 1200px;
    background: var(--page);
  }
  .artboard {
    position: absolute;
    left: 130px;
    top: 130px;
    width: 964px;
    height: 964px;
    border: 3px solid var(--frame);
    box-sizing: border-box;
    overflow: hidden;
  }
  .backdrop-photo {
    position: absolute;
    inset: 0;
    background:
      linear-gradient(100deg, var(--building) 0%, #dfe4e8 22%, rgba(223,228,232,0) 48%),
      linear-gradient(180deg, var(--sky-top), var(--sky-bottom));
  }
  .house-graphic {
    position: absolute;
    left: -133px;
    top: -133px;
    width: 1200px;
    height: 1200px;
  }
  .show-name-mark {
    position: absolute;
    left: 270px;
    top: 282px;
    display: flex;
    align-items: center;
    gap: 12px;
    font-family: "Roboto Condensed", Arial, sans-serif;
    font-weight: 700;
    font-size: 34px;
    line-height: 1;
    color: var(--ink);
    letter-spacing: 0.5px;
  }
  .show-name-mark .mark-square {
    width: 26px;
    height: 26px;
    background: var(--accent-orange);
  }
  .title {
    position: absolute;
    left: 111px;
    top: 478px;
    margin: 0;
    color: var(--ink);
    line-height: 1;
  }
  .title-top {
    display: block;
    font-family: "Roboto Condensed", Arial, sans-serif;
    font-weight: 700;
    font-size: 78px;
    letter-spacing: -0.5px;
    transform: rotate(-2deg);
    transform-origin: left bottom;
  }
  .title-main {
    display: block;
    margin-top: 4px;
    margin-left: 26px;
    font-family: "Archivo Black", Arial, sans-serif;
    font-size: 138px;
    letter-spacing: -2px;
  }
  .host-band {
    position: absolute;
    left: 99px;
    top: 779px;
    width: 650px;
    height: 102px;
    background: var(--accent-orange);
    display: flex;
    align-items: center;
    justify-content: center;
    font-family: "Itim", "Comic Sans MS", cursive;
    font-size: 58px;
    color: var(--cream);
    padding-left: 20px;
    box-sizing: border-box;
  }
  .info-band {
    position: absolute;
    left: 99px;
    top: 881px;
    width: 660px;
    height: 80px;
    background: var(--band-black);
    text-align: center;
    font-family: "Open Sans", Arial, sans-serif;
    font-weight: 400;
    padding-top: 8px;
    box-sizing: border-box;
  }
  .info-label {
    display: block;
    font-size: 17px;
    color: #ffffff;
    line-height: 1.2;
  }
  .info-url {
    display: block;
    font-size: 25px;
    color: var(--url-yellow);
    line-height: 1.3;
  }
  .host-photo {
    position: absolute;
    left: 651px;
    top: 199px;
    width: 310px;
    height: 765px;
    border-radius: 90px 90px 0 0;
    background: linear-gradient(180deg, var(--suit-navy) 0%, var(--denim) 100%);
  }
</style>
</head>
<body>
<main class="cover">
  <section class="artboard">
    <div class="backdrop-photo" role="img" aria-label="Photo of a modern white apartment building against a pale blue sky"></div>

    <svg class="house-graphic" viewBox="0 0 1200 1200" aria-hidden="true">
      <polygon class="house-wall" fill="var(--house-blue)"
        points="232,480 614,262 880,412 880,1094 232,1094"/>
      <polygon class="roof-outer" fill="var(--roof-blue)"
        points="132,432 614,178 1092,416 1092,452 614,222 146,450"/>
      <polygon class="roof-inner" fill="var(--accent-orange)"
        points="134,462 614,220 1092,456 1072,492 614,262 146,488"/>
    </svg>

    <div class="show-name-mark">
      <span class="mark-square"></span>
      <span class="mark-name">Keys To The Porch</span>
    </div>

    <h1 class="title">
      <span class="title-top">Keys To The</span>
      <span class="title-main">Porch</span>
    </h1>

    <div class="host-band">with Dale Marsh</div>

    <div class="info-band">
      <span class="info-label">More information:</span>
      <span class="info-url">keystotheporch.example</span>
    </div>

    <div class="host-photo" role="img" aria-label="Photo of the host standing, smiling, in a navy blazer, light blue shirt and jeans"></div>
  </section>
</main>
</body>
</html>
```